Simple elegant feminine design - Going out on my own as a Mortgage Broker.
My thoughts are the following details on the Front, middle of the card possibly? Phone and email smaller font than my name?
Marnie Veltrin
Finance Specialist
p: 0438 215 962
e: marnie@veltrinlending.com.au
Bottom of the card
residential / commercial / equipment
I would like the Font in Rose Gold maybe white or black background? or Possibly a stone grey - are you able to do a few options? I'd like them embossed
Then I had an idea as a simple logo as per the attached if you get the idea in my scribble, my initials, capital M attached to a small v that leads/follows into a circle? Thicker Font In Rose Gold, middle of the card at the back.
Very open to ideas though and what colour you think would look better with the Rose Gold.
Thanks so much for your help, I am not very creative and savvy with this stuff :-)
Industry/Entity Type
Finance
Contact Information for Business Card
Marnie Veltrin
p: 0438 215 962
Look and feel

```html
<!DOCTYPE html>
<html lang="en">
<head>
<meta charset="utf-8">
<title>Marnie's Business Cards</title>
<link href="https://fonts.googleapis.com/css2?family=Archivo+Black&family=Fredoka:wght@600&display=swap" rel="stylesheet">
<style>
  :root {
    --page: #ffffff;
    --card: #0d0d0d;
    --card-edge: #161616;
    --rose: #f4978a;
    --ink: #ffffff;
  }
  * { margin: 0; padding: 0; box-sizing: border-box; }
  html, body {
    width: 1006px;
    height: 1200px;
    overflow: hidden;
    background: var(--page);
  }
  .sheet {
    position: relative;
    width: 1006px;
    height: 1200px;
  }
  .card {
    position: absolute;
    left: 8px;
    width: 994px;
    height: 568px;
    background: radial-gradient(ellipse at 50% 45%, var(--card-edge) 0%, var(--card) 75%);
    overflow: hidden;
  }
  .card--front { top: 19px; }
  .card--back { top: 610px; }

  .brand-mark {
    position: absolute;
    left: 0;
    width: 100%;
    text-align: center;
    font-family: "Fredoka", sans-serif;
    font-weight: 600;
    color: var(--rose);
    line-height: 1;
  }
  .card--front .brand-mark { top: 254px; font-size: 60px; }
  .card--back .brand-mark { top: 96px; font-size: 30px; }

  .holder-name {
    position: absolute;
    top: 196px;
    left: 0;
    width: 100%;
    text-align: center;
    font-family: "Fredoka", sans-serif;
    font-weight: 600;
    font-size: 58px;
    letter-spacing: 1px;
    color: var(--ink);
    line-height: 1;
  }
  .holder-role {
    position: absolute;
    top: 264px;
    left: 0;
    width: 100%;
    text-align: center;
    font-family: "Fredoka", sans-serif;
    font-weight: 600;
    font-size: 44px;
    letter-spacing: 0.5px;
    color: var(--ink);
    line-height: 1;
  }
  .contact-row {
    position: absolute;
    top: 372px;
    left: 0;
    width: 100%;
    display: flex;
    justify-content: center;
    align-items: center;
    gap: 26px;
    font-family: "Archivo Black", sans-serif;
    color: var(--ink);
  }
  .contact-item {
    display: flex;
    align-items: center;
    gap: 14px;
  }
  .contact-icon { width: 44px; height: 44px; }
  .contact-phone { font-size: 24px; letter-spacing: 0.5px; }
  .contact-email { font-size: 21px; }

  .accent-rule {
    position: absolute;
    top: 463px;
    left: 0;
    width: 100%;
    height: 9px;
    background: var(--rose);
  }
  .service-line {
    position: absolute;
    top: 505px;
    left: 0;
    width: 100%;
    text-align: center;
    font-family: "Fredoka", sans-serif;
    font-weight: 600;
    font-size: 29px;
    letter-spacing: 0.5px;
    color: var(--ink);
    line-height: 1;
  }
</style>
</head>
<body>
<main class="sheet">
  <section class="card card--front">
    <div class="brand-mark">Veltrin Lending</div>
  </section>

  <section class="card card--back">
    <div class="brand-mark">Veltrin Lending</div>
    <h1 class="holder-name">MARNIE VELTRIN</h1>
    <p class="holder-role">Finance Specialist</p>

    <div class="contact-row">
      <div class="contact-item">
        <svg class="contact-icon" viewBox="0 0 44 44" aria-hidden="true">
          <circle cx="22" cy="22" r="20" fill="none" stroke="#ffffff" stroke-width="2.5"/>
          <path d="M15.5 12.5c1-.8 2.3-.6 3 .4l2 3c.6.9.4 2-.4 2.7l-1.3 1c.9 2.3 2.6 4.2 4.9 5.3l1-1.3c.7-.8 1.9-1 2.8-.3l2.9 2.1c1 .7 1.1 2.1.3 3l-1.3 1.5c-1 1.1-2.6 1.5-4 1-6.2-2.2-10.6-7-12.3-13.2-.4-1.4 0-2.9 1.1-3.9z" fill="#ffffff"/>
        </svg>
        <span class="contact-phone">0438 215 962</span>
      </div>
      <div class="contact-item">
        <svg class="contact-icon" viewBox="0 0 44 44" aria-hidden="true">
          <circle cx="22" cy="22" r="20" fill="none" stroke="#ffffff" stroke-width="2.5"/>
          <rect x="11" y="15" width="22" height="15" rx="1.5" fill="#ffffff"/>
          <path d="M11.5 15.8 22 24l10.5-8.2" fill="none" stroke="#0d0d0d" stroke-width="1.8"/>
          <path d="M11.5 29.2 19 22.5M32.5 29.2 25 22.5" fill="none" stroke="#0d0d0d" stroke-width="1.5"/>
        </svg>
        <span class="contact-email">marnie@veltrinlending.com.au</span>
      </div>
    </div>

    <div class="accent-rule"></div>
    <p class="service-line">Residential / Commercial / Equipment</p>
  </section>
</main>
</body>
</html>
```